We need to have 2 different retractable banners designed that will be used at a variety of events. We plan to have the banners printed through printvanta.example. According to their site, specs are as follows: Retractable banners are digitally printed on 12oz double-sided smooth vinyl. While the area on the retractable banners is 33 x 78, the customer will want to provide a file that has an area of 35 x 82 to account for bleed, with 3" of that vertical bleed at the bottom of the design. Recommneded DPI is 150. Upload capacity for retractable banners is 100MP.

Banner #1: Cascade Talent Alliance logo at top; then the following text placed lower on the banner: Providing leadership that promotes and advances Oregon's workforce system. At the bottom of banner: cascadetalent alliance.example

Banner #2: Cascade Talent Alliance logo at top; then the following text placed lower on the banner: Oregon's workforce system ensures all Oregonians possess the talent needed for communities to thrive and prosper. At the bottom of banner: cascadetalentalliance.example

Color scheme: complimentary colors of the Cascade Talent Alliance logo.
Images: images representative of Oregon (for example: map of Oregon, Douglas fir trees, coastal range, etc.

I've attached a couple of previous banners created as a reference.

```html
<!DOCTYPE html>
<html lang="en">
<head>
<meta charset="utf-8">
<title>Cascade Talent Alliance – Retractable Banners</title>
<link rel="stylesheet" href="https://fonts.googleapis.com/css2?family=Montserrat:wght@500;600;800&family=Roboto:wght@400&display=swap">
<style>
  :root {
    --backdrop: #ae9bbd;
    --navy: #0a2c6e;
    --magenta: #9b0b52;
    --paper: #f3f3f3;
    --white: #ffffff;
    --forest-dark: #1f4a22;
    --forest-mid: #4d7f3a;
    --forest-light: #9cb86a;
    --sea-deep: #1c8fbf;
    --sea-bright: #3ed0e6;
    --cliff: #c9bda5;
  }
  * { box-sizing: border-box; margin: 0; padding: 0; }
  html, body { width: 1200px; height: 1200px; overflow: hidden; }
  body {
    background: var(--backdrop);
    font-family: "Montserrat", sans-serif;
    position: relative;
  }
  .banner {
    position: absolute;
    top: 56px;
    width: 460px;
    height: 1100px;
    background: var(--navy);
    overflow: hidden;
  }
  .banner--leadership { left: 110px; }
  .banner--talent { left: 630px; }

  .banner__photo {
    position: absolute; left: 0; right: 0; top: 140px; height: 508px; z-index: 1;
  }
  .photo--fir {
    background: radial-gradient(ellipse at 45% 50%, var(--forest-light) 0%, var(--forest-mid) 35%, var(--forest-dark) 100%);
  }
  .photo--coast {
    background: linear-gradient(180deg, #cfe1ea 0%, #9fbccb 22%, var(--cliff) 38%, #b3a588 50%, var(--sea-bright) 66%, var(--sea-deep) 100%);
  }

  .banner__header {
    position: absolute; inset: 0 0 auto 0; height: 300px; z-index: 2;
  }
  .banner__swoosh { position: absolute; inset: 0; width: 460px; height: 300px; }

  .brand {
    position: absolute; top: 34px; left: 0; right: 0;
    display: flex; flex-direction: column; align-items: center; z-index: 3;
  }
  .brand__mark {
    width: 72px; height: 72px; border-radius: 8px; background: var(--magenta);
  }
  .brand__name {
    margin-top: 20px;
    font-weight: 600;
    font-size: 19px;
    letter-spacing: 3px;
    text-transform: uppercase;
    color: var(--navy);
  }

  .banner__divider {
    position: absolute; left: 0; right: 0; top: 648px; height: 3px; background: var(--paper); z-index: 1;
  }

  .message {
    position: absolute; left: 0; right: 0; top: 720px; text-align: center; color: var(--white);
  }
  .message__eyebrow {
    display: flex; align-items: center; gap: 10px;
    font-weight: 500; font-size: 16px; letter-spacing: 3px; text-transform: uppercase;
  }
  .message__eyebrow::before, .message__eyebrow::after {
    content: ""; flex: 1; height: 2px; background: var(--magenta);
  }
  .message__eyebrow--compact { font-size: 14px; letter-spacing: 1px; }
  .message__lead {
    font-weight: 800; text-transform: uppercase; line-height: 1.1; margin-top: 10px;
  }
  .message__lead span { display: block; }
  .message__lead .xl { font-size: 49px; letter-spacing: 1px; }
  .message__lead .lg { font-size: 36px; letter-spacing: 1px; margin-top: 6px; }
  .message__lead .xl-alt { font-size: 45px; letter-spacing: 1px; margin-top: 14px; }
  .message__lead .md { font-size: 29px; letter-spacing: 0.5px; margin-top: 9px; }
  .message__tag {
    margin-top: 16px; background: var(--magenta); height: 24px; line-height: 24px;
    font-weight: 600; font-size: 15px; letter-spacing: 3px; text-transform: uppercase;
  }
  .message__tag--compact { font-size: 13px; letter-spacing: 0.5px; font-weight: 500; margin-top: 20px; }

  .banner__url {
    position: absolute; left: 0; right: 0; top: 1060px; text-align: center;
    font-family: "Roboto", sans-serif; font-size: 18px; color: var(--white);
  }
</style>
</head>
<body>

<section class="banner banner--leadership">
  <div class="banner__photo photo--fir" role="img" aria-label="Close-up of a Douglas fir cone hanging among green needles"></div>
  <div class="banner__header">
    <svg class="banner__swoosh" viewBox="0 0 460 300" aria-hidden="true">
      <path d="M0 0 H460 V150 Q300 250 170 252 Q80 250 0 198 Z" fill="var(--paper)"/>
      <path d="M0 198 Q80 250 170 252 L170 262 L0 264 Z" fill="var(--magenta)"/>
      <path d="M0 272 Q260 270 460 200 V150 Q300 250 170 252 Q80 258 0 264 Z" fill="var(--navy)"/>
    </svg>
  </div>
  <div class="brand">
    <div class="brand__mark"></div>
    <div class="brand__name">Cascade Talent Alliance</div>
  </div>
  <div class="banner__divider"></div>
  <div class="message">
    <p class="message__eyebrow">Providing</p>
    <h2 class="message__lead">
      <span class="xl">Leadership</span>
      <span class="lg">That promotes</span>
      <span class="lg">and advances</span>
    </h2>
    <p class="message__tag">Oregon's workforce system.</p>
  </div>
  <p class="banner__url">cascadetalentalliance.example</p>
</section>

<section class="banner banner--talent">
  <div class="banner__photo photo--coast" role="img" aria-label="Aerial view of rugged coastal cliffs above a turquoise cove and sandy beach"></div>
  <div class="banner__header">
    <svg class="banner__swoosh" viewBox="0 0 460 300" aria-hidden="true">
      <path d="M0 0 H460 V150 Q300 250 170 252 Q80 250 0 198 Z" fill="var(--paper)"/>
      <path d="M0 198 Q80 250 170 252 L170 262 L0 264 Z" fill="var(--magenta)"/>
      <path d="M0 272 Q260 270 460 200 V150 Q300 250 170 252 Q80 258 0 264 Z" fill="var(--navy)"/>
    </svg>
  </div>
  <div class="brand">
    <div class="brand__mark"></div>
    <div class="brand__name">Cascade Talent Alliance</div>
  </div>
  <div class="banner__divider"></div>
  <div class="message">
    <p class="message__eyebrow message__eyebrow--compact">Oregon's workforce system</p>
    <h2 class="message__lead">
      <span class="xl-alt">Ensures all</span>
      <span class="md">Oregonians possess</span>
      <span class="md">the talent needed</span>
    </h2>
    <p class="message__tag message__tag--compact">For communities to thrive and prosper.</p>
  </div>
  <p class="banner__url">cascadetalentalliance.example</p>
</section>

</body>
</html>
```